I'm a magician . hypnotist also a good barber. I need this all to be shown in good detail on the cards.

Magician

Magician/ hypnotist/barber Morris quill. One of the best. Tel 07412 638204
Email.Velvetowl27@postmail-example.net
Title of card velvet owl.

```html
<!DOCTYPE html>
<html lang="en">
<head>
<meta charset="utf-8">
<title>Velvet Owl – Business Card</title>
<link rel="stylesheet" href="https://fonts.googleapis.com/css2?family=Oswald:wght@300;600&family=Open+Sans:wght@700&family=Montserrat:wght@400&display=swap">
<style>
  :root {
    --backdrop: #e7e8ea;
    --card: #ffffff;
    --ink: #0b0b0b;
    --red: #e63329;
    --red-soft: #b2412f;
    --spiral-blue: #2f5fae;
    --spiral-dark: #0a0a14;
    --hat-red: #d9362a;
  }
  * { margin: 0; padding: 0; box-sizing: border-box; }
  html, body {
    width: 1200px;
    height: 1000px;
    overflow: hidden;
    background: var(--backdrop);
  }
  .business-card {
    position: absolute;
    left: 240px;
    top: 268px;
    width: 720px;
    height: 464px;
    background: var(--card);
    text-align: center;
  }
  .emblem {
    position: absolute;
    left: 290px;
    top: 50px;
    width: 140px;
    height: 150px;
  }
  .brand-name {
    position: absolute;
    left: 0; right: 0;
    top: 188px;
    font-family: "Oswald", sans-serif;
    font-weight: 600;
    font-size: 44px;
    line-height: 56px;
    color: var(--ink);
    text-transform: uppercase;
    letter-spacing: 0.5px;
  }
  .services {
    position: absolute;
    left: 0; right: 0;
    top: 244px;
    font-family: "Oswald", sans-serif;
    font-weight: 300;
    font-size: 22px;
    line-height: 28px;
    color: var(--ink);
    letter-spacing: 2px;
  }
  .person-name {
    position: absolute;
    left: 0; right: 0;
    top: 302px;
    font-family: "Open Sans", sans-serif;
    font-weight: 700;
    font-size: 31px;
    line-height: 38px;
    color: var(--red);
    text-transform: uppercase;
    letter-spacing: -0.5px;
  }
  .tagline {
    position: absolute;
    left: 0; right: 0;
    top: 336px;
    font-family: "Oswald", sans-serif;
    font-weight: 300;
    font-size: 33px;
    line-height: 40px;
    color: var(--red-soft);
    letter-spacing: 2px;
  }
  .contact-row {
    position: absolute;
    left: 0; right: 0;
    top: 412px;
    display: flex;
    justify-content: center;
    align-items: center;
    gap: 24px;
    font-family: "Montserrat", sans-serif;
    font-weight: 400;
    font-size: 22px;
    color: var(--ink);
  }
  .contact-item {
    display: flex;
    align-items: center;
    gap: 6px;
  }
  .contact-icon { width: 30px; height: 30px; flex: none; }
</style>
</head>
<body>
  <main class="business-card">
    <svg class="emblem" viewBox="0 0 140 150" role="img" aria-label="Illustration of a red magician's top hat with gloved hands holding a wand and scissors over a blue and black hypnotic spiral">
      <defs>
        <radialGradient id="spiral-tone" cx="50%" cy="45%" r="55%">
          <stop offset="0%" stop-color="var(--spiral-dark)"/>
          <stop offset="70%" stop-color="var(--spiral-blue)"/>
          <stop offset="100%" stop-color="var(--spiral-dark)"/>
        </radialGradient>
      </defs>
      <circle cx="70" cy="70" r="70" fill="url(#spiral-tone)"/>
    </svg>

    <h1 class="brand-name">Velvet Owl</h1>
    <p class="services">MAGICIAN / HYPNOTIST / BARBER</p>

    <p class="person-name">Morris Quill</p>
    <p class="tagline">ONE OF THE BEST</p>

    <div class="contact-row">
      <span class="contact-item">
        <svg class="contact-icon" viewBox="0 0 30 30" aria-hidden="true">
          <circle cx="15" cy="15" r="15" fill="var(--ink)"/>
          <path d="M10.5 7.5c.6-.4 1.3-.3 1.7.3l1.6 2.6c.3.6.2 1.2-.3 1.6l-1.1.9c.6 1.9 1.9 3.7 3.6 4.9l1-1c.5-.4 1.1-.5 1.6-.1l2.5 1.7c.6.4.7 1.2.3 1.7l-1.2 1.5c-.6.7-1.6 1-2.5.7-4.5-1.6-7.9-5.3-9.2-9.9-.2-.9.1-1.8.8-2.4z" fill="#fff"/>
        </svg>
        07412 638204
      </span>
      <span class="contact-item">
        <svg class="contact-icon" viewBox="0 0 30 30" aria-hidden="true">
          <circle cx="15" cy="15" r="15" fill="var(--ink)"/>
          <rect x="7.5" y="9.5" width="15" height="11" rx="1" fill="#fff"/>
          <path d="M7.8 10l7.2 5.6 7.2-5.6" fill="none" stroke="var(--ink)" stroke-width="1.4"/>
          <path d="M7.8 20l5.3-5M22.2 20l-5.3-5" fill="none" stroke="var(--ink)" stroke-width="1.2"/>
        </svg>
        Velvetowl27@postmail-example.net
      </span>
    </div>
  </main>
</body>
</html>
```